Pitch Deck and business cards for Virtual Reality Startup

We need a redesign of our pitch deck to be funky, creative and interactive with animated graphics inline with our product (VR training)
Note: the design does not have to be orange that's just a template of the information we're sending you so we would like to see other colours also.

Target Market(s)

Investors

Industry/Entity Type

Media

Contact Information for Business Card

logo, Name, title, address, telephone, email, website

Font styles to use
Other font styles liked:
• funky but readable

Colors

Designer to choose colors to be used in the design.

Requirements
Must have
• Exciting non traditional design that fits a new, innovative, exciting and interactive technology
Nice to have
• .
Should not have
• traditional look and feel.

```html
<!DOCTYPE html>
<html lang="en">
<head>
<meta charset="utf-8">
<title>NOVAREAL – Pitch Deck and Business Cards</title>
<link rel="stylesheet" href="https://fonts.googleapis.com/css2?family=Archivo:wght@400;500;600;700;800&display=swap">
<style>
  :root{
    --orange:#e87722;
    --orange-deep:#d9661a;
    --orange-soft:#f0a468;
    --ink:#1c1c1c;
    --grey:#7a7a7a;
    --white:#ffffff;
    --board:#c4c4c4;
  }
  *{box-sizing:border-box;margin:0;padding:0}
  html,body{width:1200px;height:1097px;overflow:hidden;background:var(--board)}
  body{font-family:"Archivo",Arial,sans-serif;position:relative}
  .slide{position:absolute;width:387px;height:217px;overflow:hidden;background:var(--white);
    box-shadow:0 6px 14px rgba(0,0,0,.35);border-bottom:5px solid var(--orange)}
  .slide svg.bg{position:absolute;inset:0;width:100%;height:100%}
  .abs{position:absolute}
  .mini-logo{position:absolute;right:10px;top:6px;font-weight:800;font-size:8px;line-height:9px;letter-spacing:.5px;color:var(--ink)}
  .mini-logo::after{content:"";display:inline-block;width:6px;height:6px;background:var(--ink);margin-left:3px;vertical-align:0}
  .photo{position:absolute}
  /* title slide */
  .s-title{left:10px;top:12px;background:var(--orange)}
  .s-title .brand{left:14px;top:36px;font-size:30px;font-weight:800;color:var(--ink);letter-spacing:1px}
  .s-title .brand::after{content:"";display:inline-block;width:16px;height:16px;background:var(--ink);margin-left:6px}
  .s-title h1{left:13px;top:88px;font-size:25px;line-height:29px;font-weight:800;color:var(--white)}
  .s-title .badge{left:6px;top:188px;width:24px;height:24px;background:#bdbdbd}
  /* story */
  .s-story{left:404px;top:12px}
  .s-story h2{left:0;right:0;top:10px;text-align:center;font-size:37px;font-weight:800;color:var(--white)}
  /* problem */
  .s-problem{left:799px;top:12px;background:var(--orange)}
  .s-problem .label{left:10px;top:102px;width:110px;text-align:center;font-size:19px;line-height:20px;font-weight:800;color:var(--orange)}
  .s-problem .lead{left:210px;top:40px;width:165px;text-align:center;font-size:16px;line-height:19px;font-weight:700;color:var(--white)}
  .s-problem .big{left:200px;top:138px;width:185px;text-align:center;font-size:28px;font-weight:800;color:var(--white)}
  /* traditional */
  .s-trad{left:10px;top:243px}
  .s-trad h2{left:225px;top:78px;width:160px;text-align:center;font-size:26px;line-height:29px;font-weight:700;color:var(--ink)}
  /* vr */
  .s-vr{left:404px;top:243px}
  .s-vr h2{left:26px;top:62px;font-size:25px;line-height:29px;font-weight:700;color:var(--ink)}
  .s-vr ul{left:188px;top:38px;list-style:none}
  .s-vr li{font-size:13px;font-weight:700;color:var(--white);height:29px;display:flex;align-items:center;gap:5px}
  .s-vr li svg{width:14px;height:14px}
  /* team */
  .s-team{left:799px;top:243px;background:var(--orange)}
  .s-team .strip{left:16px;top:0;width:45px;height:217px;background:var(--white)}
  .s-team .strip span{position:absolute;left:22px;top:108px;transform:translate(-50%,-50%) rotate(-90deg);white-space:nowrap;font-size:15px;font-weight:700;color:var(--ink)}
  .s-team .band{left:61px;width:326px;height:48px;background:var(--ink)}
  .member{position:absolute;width:90px;margin-left:-45px;text-align:center;color:var(--white)}
  .member .head{width:36px;height:36px;border-radius:50%;background:linear-gradient(#d8d8d8,#9a9a9a);border:2px solid var(--white);margin:0 auto 4px}
  .member b{display:block;font-size:5px;font-weight:700;text-transform:uppercase}
  .member i{display:block;font-style:normal;font-size:4px;line-height:5px}
  /* process */
  .s-process{left:10px;top:469px}
  .s-process h2{left:8px;top:52px;width:130px;text-align:center;font-size:27px;line-height:31px;font-weight:700;color:var(--white)}
  .cycle-label{position:absolute;transform:translate(-50%,-50%);text-align:center;font-size:5.5px;line-height:6.5px;font-weight:700;color:var(--white);white-space:nowrap}
  /* business */
  .s-biz{left:404px;top:469px}
  .s-biz h2{left:0;right:0;top:18px;text-align:center;font-size:28px;font-weight:700;color:var(--ink)}
  .s-biz .band-text{position:absolute;text-align:center;font-size:17px;line-height:18px;font-weight:700;color:var(--white)}
  /* ask */
  .s-ask{left:799px;top:469px}
  .s-ask .ask{left:68px;top:80px;width:70px;text-align:center;font-size:20px;line-height:21px;font-weight:700;color:var(--ink)}
  .pill-text{position:absolute;font-size:11px;font-weight:700;color:var(--white)}
  /* questions */
  .s-q{left:404px;top:694px;background:var(--orange)}
  .s-q h2{left:0;right:0;top:58px;text-align:center;font-size:44px;font-weight:800;color:var(--white)}
  .s-q .mark{left:0;right:0;top:112px;text-align:center;font-size:52px;font-weight:800;color:var(--white)}
  /* cards */
  .card{position:absolute;width:249px;height:147px;overflow:hidden;box-shadow:0 5px 12px rgba(0,0,0,.35);background:var(--orange)}
  .card-front{left:880px;top:768px}
  .card-back{left:880px;top:929px}
  .card-front .brand{left:13px;top:66px;font-size:12px;font-weight:800;color:var(--ink);letter-spacing:0;white-space:nowrap}
  .card-front .brand::after,.card-back .brand::after{content:"";display:inline-block;background:var(--ink);margin-left:4px}
  .card-front .brand::after{width:7px;height:7px}
  .contact{position:absolute;left:128px;font-size:7.5px;line-height:8px;color:var(--ink)}
  .contact.name{font-size:9px;font-weight:700;line-height:9px}
  .contact.name span{display:block;font-size:7.5px;font-weight:400}
  .card-back .brand{left:0;right:0;top:56px;text-align:center;font-size:30px;font-weight:800;color:var(--ink);letter-spacing:1px}
  .card-back .brand::after{width:18px;height:18px}
</style>
</head>
<body>

<!-- Title -->
<section class="slide s-title">
  <div class="photo" role="img" aria-label="Photo of a young man wearing a VR headset" style="left:205px;top:0;width:182px;height:217px;background:linear-gradient(90deg,rgba(232,119,34,0),#b26a3e 35%,#4a5563 85%)"></div>
  <div class="abs brand">NOVAREAL</div>
  <h1 class="abs">THE FUTURE OF<br>HOSPITALITY<br>TRAINING</h1>
  <div class="abs badge"></div>
</section>

<!-- Story -->
<section class="slide s-story">
  <svg class="bg" viewBox="0 0 387 217" preserveAspectRatio="none">
    <rect width="387" height="217" fill="var(--orange)"/>
    <path d="M0 135 C40 115 100 118 150 140 C210 165 260 100 300 95 C340 90 370 130 387 135 L387 217 L0 217 Z" fill="var(--white)"/>
  </svg>
  <div class="mini-logo">NOVAREAL</div>
  <h2 class="abs">Mary’s story…</h2>
  <div class="photo" role="img" aria-label="News article clipping with headline and photo of two men" style="left:116px;top:67px;width:154px;height:139px;background:linear-gradient(#fff 0 22%,#6f8a5a 22%,#9aa889 60%,#c9c4cf 100%);box-shadow:0 2px 6px rgba(0,0,0,.3)"></div>
</section>

<!-- Problem -->
<section class="slide s-problem">
  <svg class="bg" viewBox="0 0 387 217" preserveAspectRatio="none">
    <path d="M0 0 L218 0 C236 40 200 80 190 110 C176 150 200 190 138 217 L0 217 Z" fill="#2a2a2a"/>
  </svg>
  <div class="photo" role="img" aria-label="Black and white photo of a man in a suit adjusting his tie" style="left:0;top:0;width:190px;height:217px;background:radial-gradient(circle at 60% 40%,#5a5a5a,#222 70%);opacity:.85;clip-path:polygon(0 0,100% 0,100% 60%,70% 100%,0 100%)"></div>
  <div class="mini-logo">NOVAREAL</div>
  <div class="abs label">THE<br>PROBLEM</div>
  <div class="abs lead">Traditional training does not prepare staff to be</div>
  <div class="abs big">Job Ready</div>
</section>

<!-- Traditional training -->
<section class="slide s-trad">
  <div class="photo" role="img" aria-label="Orange-tinted photo of a bored student resting his head on a desk" style="left:0;top:0;width:290px;height:217px;background:linear-gradient(120deg,#f0a060,#e07a35 60%,#c96a2c)"></div>
  <svg class="bg" viewBox="0 0 387 217" preserveAspectRatio="none">
    <path d="M200 0 L387 0 L387 217 L278 217 C225 190 212 150 222 112 C232 72 225 30 200 0 Z" fill="var(--white)"/>
  </svg>
  <h2 class="abs">Traditional training</h2>
</section>

<!-- VR training -->
<section class="slide s-vr">
  <svg class="bg" viewBox="0 0 387 217" preserveAspectRatio="none">
    <path d="M98 0 L387 0 L387 217 L165 217 C175 170 170 140 180 110 C190 70 160 20 98 0 Z" fill="var(--orange)"/>
  </svg>
  <div class="mini-logo">NOVAREAL</div>
  <h2 class="abs">Virtual<br>reality<br>training</h2>
  <ul class="abs">
    <li><svg viewBox="0 0 14 14"><circle cx="7" cy="7" r="7" fill="#fff"/><path d="M3.5 7.2 L6 9.6 L10.6 4.6" stroke="var(--orange)" stroke-width="1.8" fill="none"/></svg>Retention of knowledge</li>
    <li><svg viewBox="0 0 14 14"><circle cx="7" cy="7" r="7" fill="#fff"/><path d="M3.5 7.2 L6 9.6 L10.6 4.6" stroke="var(--orange)" stroke-width="1.8" fill="none"/></svg>Real-life experiences</li>
    <li><svg viewBox="0 0 14 14"><circle cx="7" cy="7" r="7" fill="#fff"/><path d="M3.5 7.2 L6 9.6 L10.6 4.6" stroke="var(--orange)" stroke-width="1.8" fill="none"/></svg>Immersive &amp; engaging</li>
  </ul>
  <div class="photo" role="img" aria-label="Photo of two people wearing VR headsets" style="left:170px;top:115px;width:190px;height:102px;background:radial-gradient(ellipse at 50% 70%,#e6e6e6,rgba(232,119,34,0) 70%)"></div>
</section>

<!-- Team -->
<section class="slide s-team">
  <div class="abs strip"><span>What makes us unique?</span></div>
  <div class="abs band" style="top:57px"></div>
  <div class="abs band" style="top:148px"></div>
  <div class="mini-logo">NOVAREAL</div>
  <div class="member" style="left:126px;top:40px"><div class="head" role="img" aria-label="Team member portrait"></div><b>Grant Holloway</b><i>Co Founder and CEO</i></div>
  <div class="member" style="left:224px;top:40px"><div class="head" role="img" aria-label="Team member portrait"></div><b>Dr Irene Castellan</b><i>Learning and Development Strategist</i></div>
  <div class="member" style="left:328px;top:40px"><div class="head" role="img" aria-label="Team member portrait"></div><b>Marion Delacroix</b><i>Co Founder, Education and Content Director</i></div>
  <div class="member" style="left:126px;top:127px"><div class="head" role="img" aria-label="Team member portrait"></div><b>Luca Ferrante</b><i>360 Film and Post-Production Expert</i></div>
  <div class="member" style="left:224px;top:127px"><div class="head" role="img" aria-label="Team member portrait"></div><b>Sofia Marenko</b><i>Learning Designer</i></div>
  <div class="member" style="left:328px;top:127px"><div class="head" role="img" aria-label="Team member portrait"></div><b>Kenji Moriyama</b><i>Programmer and Game Developer</i></div>
</section>

<!-- Process -->
<section class="slide s-process">
  <svg class="bg" viewBox="0 0 387 217" preserveAspectRatio="none">
    <path d="M0 0 L150 0 C138 20 178 40 162 72 C150 100 168 122 150 142 C130 168 102 150 82 172 C60 196 30 150 0 156 Z" fill="var(--orange)"/>
    <g fill="none" stroke-width="40" transform="translate(270 104)">
      <circle r="70" pathLength="8" stroke-dasharray="0.95 7.05" stroke="var(--orange)" transform="rotate(-135)"/>
      <circle r="70" pathLength="8" stroke-dasharray="0.95 7.05" stroke="var(--ink)" transform="rotate(-90)"/>
      <circle r="70" pathLength="8" stroke-dasharray="0.95 7.05" stroke="var(--orange)" transform="rotate(-45)"/>
      <circle r="70" pathLength="8" stroke-dasharray="0.95 7.05" stroke="var(--ink)" transform="rotate(0)"/>
      <circle r="70" pathLength="8" stroke-dasharray="0.95 7.05" stroke="var(--orange)" transform="rotate(45)"/>
      <circle r="70" pathLength="8" stroke-dasharray="0.95 7.05" stroke="var(--ink)" transform="rotate(90)"/>
      <circle r="70" pathLength="8" stroke-dasharray="0.95 7.05" stroke="var(--orange)" transform="rotate(135)"/>
      <circle r="70" pathLength="8" stroke-dasharray="0.95 7.05" stroke="var(--ink)" transform="rotate(180)"/>
    </g>
  </svg>
  <div class="mini-logo">NOVAREAL</div>
  <h2 class="abs">Our<br>Process</h2>
  <div class="cycle-label" style="left:243px;top:40px">Release</div>
  <div class="cycle-label" style="left:297px;top:40px">Research<br>topics</div>
  <div class="cycle-label" style="left:334px;top:78px">Create<br>Content</div>
  <div class="cycle-label" style="left:334px;top:130px">Learning<br>Design</div>
  <div class="cycle-label" style="left:297px;top:168px">360 Film<br>Production</div>
  <div class="cycle-label" style="left:243px;top:168px">360 Post<br>Production</div>
  <div class="cycle-label" style="left:206px;top:130px">Interactive<br>Gaming<br>Development</div>
  <div class="cycle-label" style="left:206px;top:78px">Testing</div>
</section>

<!-- Business model -->
<section class="slide s-biz">
  <svg class="bg" viewBox="0 0 387 217" preserveAspectRatio="none">
    <path d="M0 68 L280 68 A28.5 28.5 0 0 1 280 125 L0 125 Z" fill="var(--orange)"/>
    <circle cx="280" cy="97" r="22" fill="var(--ink)"/>
    <g fill="#fff">
      <circle cx="271" cy="89" r="3"/><rect x="268" y="93" width="6" height="11" rx="2"/>
      <circle cx="289" cy="89" r="3"/><rect x="286" y="93" width="6" height="11" rx="2"/>
      <circle cx="280" cy="92" r="2.5"/><rect x="277.5" y="95" width="5" height="9" rx="2"/>
    </g>
    <path d="M108 134 L387 134 L387 190 L108 190 A28 28 0 0 1 108 134 Z" fill="var(--orange)"/>
    <circle cx="109" cy="162" r="22" fill="var(--ink)"/>
    <circle cx="106" cy="166" r="8" fill="none" stroke="#fff" stroke-width="1.5"/>
    <path d="M112 160 L112 150 M108 154 L112 149 L116 154" stroke="#fff" stroke-width="2" fill="none"/>
    <text x="106" y="169.5" font-family="Archivo, sans-serif" font-size="10" font-weight="700" fill="#fff" text-anchor="middle">$</text>
  </svg>
  <div class="mini-logo">NOVAREAL</div>
  <h2 class="abs">Business model</h2>
  <div class="band-text" style="left:30px;top:79px;width:200px">Partnerships with<br>training providers</div>
  <div class="band-text" style="left:135px;top:146px;width:245px;font-size:16px">Subscription based with new<br>content released monthly</div>
</section>

<!-- Our ask -->
<section class="slide s-ask">
  <svg class="bg" viewBox="0 0 387 217" preserveAspectRatio="none">
    <path d="M140 60 L178 37 L212 37" stroke="var(--ink)" stroke-width="3" fill="none"/>
    <path d="M165 104 L212 104" stroke="var(--orange)" stroke-width="3" fill="none"/>
    <path d="M126 128 L168 170 L212 170" stroke="var(--grey)" stroke-width="3" fill="none"/>
    <circle cx="103" cy="104" r="64" fill="none" stroke="var(--ink)" stroke-width="6"/>
    <circle cx="103" cy="104" r="50" fill="none" stroke="var(--orange)" stroke-width="9"/>
    <circle cx="103" cy="104" r="37" fill="#fff" stroke="var(--grey)" stroke-width="5"/>
    <rect x="212" y="18" width="138" height="39" rx="19.5" fill="var(--ink)"/>
    <circle cx="229" cy="37" r="19" fill="var(--ink)" stroke="#fff" stroke-width="2"/>
    <path d="M219 37 L226 31 L232 35 L239 31 M223 40 L229 44 L237 38" stroke="#fff" stroke-width="2" fill="none"/>
    <rect x="212" y="84" width="138" height="40" rx="20" fill="var(--orange)"/>
    <circle cx="229" cy="104" r="20" fill="var(--orange)" stroke="#fff" stroke-width="2"/>
    <path d="M219 112 L227 108 L238 108" stroke="#fff" stroke-width="2.5" fill="none"/>
    <text x="229" y="105" font-family="Archivo, sans-serif" font-size="11" font-weight="700" fill="#fff" text-anchor="middle">$</text>
    <rect x="212" y="151" width="138" height="40" rx="20" fill="var(--grey)"/>
    <circle cx="229" cy="171" r="20" fill="var(--grey)" stroke="#fff" stroke-width="2"/>
    <g fill="#fff"><circle cx="224" cy="166" r="3.5"/><path d="M217 178 a7 6 0 0 1 14 0 Z"/><circle cx="234" cy="166" r="3.5"/><path d="M227 178 a7 6 0 0 1 14 0 Z"/></g>
  </svg>
  <div class="mini-logo">NOVAREAL</div>
  <div class="abs ask">Our<br>ask</div>
  <div class="pill-text" style="left:263px;top:30px">Introductions</div>
  <div class="pill-text" style="left:278px;top:96px">Funding</div>
  <div class="pill-text" style="left:274px;top:163px">Investors</div>
</section>

<!-- Questions -->
<section class="slide s-q">
  <div class="photo" role="img" aria-label="Faded photo of a woman using a VR headset at a desk" style="left:0;top:0;width:387px;height:217px;background:linear-gradient(90deg,var(--orange) 20%,#eda26d 70%,#f2c3a0)"></div>
  <div class="mini-logo">NOVAREAL</div>
  <h2 class="abs">Questions</h2>
  <div class="abs mark">?</div>
</section>

<!-- Business card front -->
<div class="card card-front">
  <svg class="abs" style="inset:0" width="249" height="147" viewBox="0 0 249 147">
    <rect x="106" y="0" width="143" height="147" fill="#fff"/>
    <path d="M104 0 L122 0 L122 140 L113 147 L104 140 Z" fill="var(--ink)"/>
    <path d="M96 0 L130 0 L113 10 Z" fill="var(--ink)"/>
    <g fill="#fff">
      <circle cx="113" cy="17" r="2.5"/><path d="M108.5 24 a4.5 4 0 0 1 9 0 Z"/>
      <rect x="110" y="43" width="6" height="10" rx="1"/>
      <rect x="109" y="69" width="8" height="6"/>
      <path d="M110 90 L110 101 L112.5 98.5 L115 103 L116.5 102 L114 97.5 L117 97 Z"/>
      <path d="M113 113 a4 4 0 0 1 4 4 c0 3 -4 7 -4 7 c0 0 -4 -4 -4 -7 a4 4 0 0 1 4 -4 Z"/>
    </g>
    <rect x="111" y="44.5" width="4" height="6" fill="var(--ink)"/>
    <path d="M109 69 L113 72.5 L117 69" stroke="var(--ink)" stroke-width="1" fill="none"/>
    <circle cx="113" cy="117" r="1.5" fill="var(--ink)"/>
  </svg>
  <div class="abs brand">NOVAREAL</div>
  <div class="contact name" style="top:15px">YOUR NAME<span>Job Position</span></div>
  <div class="contact" style="top:44px">(820) 000 000</div>
  <div class="contact" style="top:68px">youremail@email.com</div>
  <div class="contact" style="top:92px">www.novareal.com.au</div>
  <div class="contact" style="top:114px">1000 Any Avenue<br>GREEN BAY, NY 00000</div>
</div>

<!-- Business card back -->
<div class="card card-back">
  <svg class="abs" style="inset:0" width="249" height="147" viewBox="0 0 249 147">
    <path d="M100 0 L150 0 L125 16 Z" fill="var(--ink)"/>
    <path d="M90 147 L160 147 L125 131 Z" fill="var(--ink)"/>
  </svg>
  <div class="abs brand">NOVAREAL</div>
</div>

</body>
</html>
```